Personalised Poetry business needs a business card designed

I am a writer that specialises in personalised poetry for people for significant life events.
I want a business card that stands out and portrays class and professionalism but is also welcoming & indicates warmth and honesty.
I'm happy with the logo that was designed for me, I would like to see it in raised print on the business card. I am open to suggestions on colours but think perhaps gold or silver writing for the logo would look good. I would like just the logo and my name and contact details on the front of the card. On the back of the card, I would like a list of the different events I provide poems for I will upload a photo of my current business card for reference. My current logo has a shading behind it that I don't like, I just want the words of the logo without any background colour

Target Market(s)

People wanting to provide a unique gift to someone special in their life

Industry/Entity Type

Writer

Contact Information for Business Card

Logo, my name and contact details on the front and a list of all the events I write poetry for on the back

Font styles to use
Script

Requirements
Must have
• I would like to see the logo, if possible, in a raised type of print on the card so that you can feel the actual words. I would like to have a glossy finish to the card and be able to print it on good quality board
Should not have
• The shading that is currently behind the logo on my current business card

```html
<!DOCTYPE html>
<html lang="en">
<head>
<meta charset="utf-8">
<title>Rhymes for Always – Business Card</title>
<link rel="stylesheet" href="https://fonts.googleapis.com/css2?family=Roboto:ital,wght@0,400;0,700;1,400&family=Yellowtail&display=swap">
<style>
  :root {
    --stage: #000000;
    --card-dark: #3b3b3b;
    --card-light: #ffffff;
    --ink-dark: #2e2e2e;
    --ink-light: #ffffff;
    --silver-hi: #f2f2f2;
    --silver-mid: #cfcfcf;
    --silver-lo: #a8a8a8;
    --mist: #ececec;
  }
  * { margin: 0; padding: 0; box-sizing: border-box; }
  html, body {
    width: 1200px; height: 1200px; overflow: hidden;
    background: var(--stage);
    font-family: "Roboto", Arial, sans-serif;
  }
  .card {
    position: absolute; left: 169px;
    width: 862px; height: 503px; overflow: hidden;
  }
  .card--front { top: 69px; background: var(--card-dark); }
  .card--back { top: 627px; background: var(--card-light); }

  .card__decor { position: absolute; }
  .card--front .card__decor {
    left: 0; top: 220px; width: 510px; height: 283px;
    background: linear-gradient(60deg, var(--silver-hi) 0%, var(--silver-lo) 45%, var(--silver-hi) 75%, var(--silver-mid) 100%);
  }
  .card--back .card__decor {
    left: 0; top: 160px; width: 560px; height: 343px;
    background: linear-gradient(180deg, var(--mist) 0%, var(--card-light) 70%);
  }

  .brand { position: absolute; text-align: center; }
  .brand__name {
    display: flex; align-items: center; gap: 12px;
    font-size: 42px; font-weight: 400; letter-spacing: 0.5px;
  }
  .brand__dot { width: 14px; height: 14px; border-radius: 50%; }
  .brand__tagline { font-size: 19px; margin-top: 6px; }
  .card--front .brand { left: 400px; top: 70px; color: var(--ink-light); }
  .card--front .brand__dot { background: var(--ink-light); }
  .card--back .brand { left: 420px; top: 70px; color: var(--ink-dark); }
  .card--back .brand__dot { background: var(--ink-dark); }

  .holder { position: absolute; left: 79px; top: 296px; color: var(--ink-dark); }
  .holder__name { font-size: 35px; font-weight: 700; letter-spacing: 0.5px; }
  .contact { list-style: none; margin-top: 36px; }
  .contact__item {
    display: flex; align-items: center; gap: 14px;
    font-size: 21px; line-height: 34px;
  }
  .contact__icon { width: 18px; height: 18px; fill: var(--ink-dark); }

  .services {
    position: absolute; left: 58px; top: 272px;
    list-style: none; color: var(--ink-dark);
    font-style: italic; font-size: 21px; line-height: 33px;
  }
  .services__item::before { content: "»"; font-style: normal; margin-right: 9px; }

  .slogan {
    position: absolute; right: 58px; top: 236px;
    font-family: "Yellowtail", cursive;
    font-size: 37px; line-height: 47.5px; text-align: right;
    color: var(--ink-dark);
  }
</style>
</head>
<body>

<section class="card card--front" aria-label="Card front">
  <div class="card__decor" role="img" aria-label="Soft silver decorative swirl area"></div>

  <div class="brand">
    <div class="brand__name"><span class="brand__dot"></span>Rhymes for Always</div>
    <div class="brand__tagline">Personalised Poetry</div>
  </div>

  <div class="holder">
    <h1 class="holder__name">DANIEL MARSH</h1>
    <ul class="contact">
      <li class="contact__item">
        <svg class="contact__icon" viewBox="0 0 24 24" aria-hidden="true"><path d="M6.6 10.8a15.1 15.1 0 0 0 6.6 6.6l2.2-2.2a1 1 0 0 1 1-.25 11.4 11.4 0 0 0 3.6.57 1 1 0 0 1 1 1V20a1 1 0 0 1-1 1A17 17 0 0 1 3 4a1 1 0 0 1 1-1h3.5a1 1 0 0 1 1 1c0 1.25.2 2.45.57 3.57a1 1 0 0 1-.25 1z"/></svg>
        0400 123 456
      </li>
      <li class="contact__item">
        <svg class="contact__icon" viewBox="0 0 24 24" aria-hidden="true"><path d="M3 5h18v14H3z"/><path d="M4 6.5l8 6 8-6" fill="none" stroke="#cfcfcf" stroke-width="1.6"/></svg>
        daniel@rhymesforalways.com
      </li>
    </ul>
  </div>
</section>

<section class="card card--back" aria-label="Card back">
  <div class="card__decor" role="img" aria-label="Soft silver decorative ribbon area"></div>

  <div class="brand">
    <div class="brand__name"><span class="brand__dot"></span>Rhymes for Always</div>
    <div class="brand__tagline">Personalised Poetry</div>
  </div>

  <ul class="services">
    <li class="services__item">Weddings &amp; Anniversaries</li>
    <li class="services__item">Birthdays &amp; Christmas</li>
    <li class="services__item">Valentines Day</li>
    <li class="services__item">Retirements, Business &amp; Corporate Events</li>
    <li class="services__item">Funerals &amp; Eulogies</li>
  </ul>

  <p class="slogan">Monentous<br>Life Events<br>Personalised<br>in Poetry</p>
</section>

</body>
</html>
```